Building Servicess

We need a new business card design for a company. We specialise in: Electrical/Site temporary electrics, Data/Network Installation, Passive Fire Protection

Industry/Entity Type

Construction

Contact Information for Business Card

Services provided as detailed on project description

Font styles to use
Serif

Colors
0054AA
0677BA
7BADD7
CADEEF
E8F1F8
00AB8E
00BBA5
67D7C9
C6EFE9
E9F9F6
EB3D1F
EC4F4E
F09395
F8D3D4
FCEDEE

Requirements
Must have
• Company logo-contact details-phone numbers

```html
<!DOCTYPE html>
<html lang="en">
<head>
<meta charset="utf-8">
<title>Norvale Site Works – Business Card</title>
<link href="https://fonts.googleapis.com/css2?family=Montserrat:ital,wght@0,700;1,800&family=Arimo:ital@0;1&display=swap" rel="stylesheet">
<style>
  :root {
    --brand-blue: #0c75bf;
    --band-grey: #858688;
    --paper: #ffffff;
    --backdrop: #26272a;
  }
  * { margin: 0; padding: 0; box-sizing: border-box; }
  html, body {
    width: 1200px; height: 900px; overflow: hidden;
    background: var(--backdrop);
  }
  .sheet {
    position: relative; width: 1200px; height: 900px;
    display: flex; flex-direction: column; align-items: center; justify-content: center; gap: 44px;
  }
  .card {
    position: relative; width: 600px; height: 343px;
    background: var(--brand-blue); overflow: hidden;
    box-shadow: 0 10px 30px rgba(0,0,0,.45);
  }

  /* front */
  .card-front { display: flex; align-items: center; justify-content: center; }
  .brand-front {
    font-family: "Montserrat", sans-serif; font-weight: 700;
    color: var(--paper); font-size: 38px; letter-spacing: 1px;
    text-transform: uppercase; text-align: center; line-height: 1.15;
  }

  /* back */
  .back-shapes { position: absolute; inset: 0; width: 100%; height: 100%; }
  .contact-block { position: absolute; left: 40px; top: 38px; color: var(--paper); }
  .person-name {
    position: relative; padding-left: 26px;
    font-family: "Montserrat", sans-serif; font-style: italic; font-weight: 800;
    font-size: 23px; letter-spacing: .5px; text-transform: uppercase; line-height: 1;
  }
  .person-name::before {
    content: ""; position: absolute; left: 0; top: 0; width: 14px; height: 24px;
    background: var(--paper); transform: skewX(-12deg);
  }
  .person-role {
    font-family: "Arimo", sans-serif; font-style: italic; font-size: 13px;
    margin: 4px 0 0 20px;
  }
  .address {
    font-family: "Arimo", sans-serif; font-style: italic; font-size: 13.5px;
    line-height: 1.3; margin-top: 48px;
  }
  .contact-list { list-style: none; margin-top: 14px; font-family: "Arimo", sans-serif; font-style: italic; font-size: 13.5px; line-height: 1.45; }
  .contact-list li { display: flex; align-items: center; gap: 7px; }
  .contact-list svg { width: 11px; height: 11px; flex: none; }
  .brand-back {
    position: absolute; left: 390px; top: 205px; width: 190px;
    font-family: "Montserrat", sans-serif; font-weight: 700;
    color: var(--brand-blue); font-size: 19px; letter-spacing: .5px;
    text-transform: uppercase; line-height: 1.2; text-align: center;
  }
</style>
</head>
<body>
<main class="sheet">
  <section class="card card-front" aria-label="Business card front">
    <p class="brand-front">Norvale Site Works<br>Ltd</p>
  </section>

  <section class="card card-back" aria-label="Business card back">
    <svg class="back-shapes" viewBox="0 0 600 343" preserveAspectRatio="none" aria-hidden="true">
      <polygon points="345,343 345,150 600,40 600,343" fill="var(--band-grey)"/>
      <polygon points="372,343 372,168 600,70 600,343" fill="var(--paper)"/>
    </svg>

    <div class="contact-block">
      <h1 class="person-name">Daniel Marsh</h1>
      <p class="person-role">Managing Director</p>
      <p class="address">118 Harbour Lane.<br>Kingsford, KF 20417</p>
      <ul class="contact-list">
        <li><svg viewBox="0 0 12 12"><rect x="3" y="0.5" width="6" height="11" rx="1" fill="none" stroke="#fff" stroke-width="1.2"/></svg>07700900418</li>
        <li><svg viewBox="0 0 12 12"><path d="M2 1l2.5 0 1 3-1.5 1a7 7 0 0 0 3 3l1-1.5 3 1 0 2.5c-5 .5-9.5-4-9-9z" fill="#fff"/></svg>020 7946 0321</li>
        <li><svg viewBox="0 0 12 12"><rect x="0.5" y="2.5" width="11" height="7" fill="#fff"/><path d="M0.5 2.5l5.5 4 5.5-4" fill="none" stroke="var(--brand-blue)" stroke-width="1"/></svg>hello@norvalesiteworks.com</li>
        <li><svg viewBox="0 0 12 12"><circle cx="6" cy="6" r="5.3" fill="none" stroke="#fff" stroke-width="1.2"/><path d="M1 6h10M6 .7c-3 3-3 7.6 0 10.6M6 .7c3 3 3 7.6 0 10.6" fill="none" stroke="#fff" stroke-width=".9"/></svg>www.norvalesiteworks.com</li>
      </ul>
    </div>

    <p class="brand-back">Norvale Site Works Ltd</p>
  </section>
</main>
</body>
</html>
```